LABEL DESIGNS FOR SKINCARE LINE

Hello we are needing 12 label various label designs but would like to see you design ONE. We will pick winner from this and send the rest.
LABEL SIZE -2x7
JAR SIZE IS - 8oz
LOGOS FILES BELOW
https://files.pavorna-share.net/drive/folders/7xk3q-wumTrazPLoqVnnRTZBKHAE2DpLW
INFORMATION FOR LABEL
Calm Dune Hush Whipped Body Sugar Scrub 8oz
Ideal for all Skin Types
Ingredients:
Pure Cane Sugar, Extra Virgin Coconut Oil, Mango Butter, Kukum Butter, Emulsifying Wax, Jojoba Seed Oil, Sweet Almond Oil, Strawberry Essential Oil, and Pomegranate Essential Oil.
Directions to use Body Sugar Scrub:
Apply to wet skin gently in a circular motion on desired body area, hands, feet, legs, arms, etc. Once you have a good scrub, rinse, pat dry, and enjoy soft, hydrated skin. Best to use in the shower. Use between 2-3 times a week if needed.
*Cautions:
(1) Allergy: Approach this product with extreme caution, if you have allergies
(2) Avoid direct contact with eyes
Storage/Shelf Life of Product:
For best results, stir/mix scrub with the wooden or plastic spoon before each use. The shelf life of all sugar scrubs is 6-8 weeks. Keep the product in a cool, dry place, away from hot or heated temperatures.
All Natural, Cruelty-Free, Vegan Free
No Mineral Oil
No Petroleum
No Parabens

```html
<!DOCTYPE html>
<html lang="en">
<head>
<meta charset="utf-8">
<title>Calm Dune Hush – Whipped Body Sugar Scrub Label</title>
<link href="https://fonts.googleapis.com/css2?family=Roboto+Condensed:wght@300;400;500;700&family=Playfair+Display:wght@500&display=swap" rel="stylesheet">
<style>
  :root {
    --label-bg: #fadbe8;
    --rose: #c5718f;
    --rose-soft: #e9a4bb;
    --band-text: #f7d9e5;
    --ink: #141414;
    --illustration: #d893ab;
  }
  html, body {
    margin: 0;
    padding: 0;
    overflow: hidden;
    background: var(--label-bg);
  }
  .label {
    position: relative;
    width: 1200px;
    height: 343px;
    overflow: hidden;
    background: var(--label-bg);
    font-family: "Roboto Condensed", "Arial Narrow", sans-serif;
    font-weight: 300;
    color: var(--ink);
  }
  .panel {
    position: absolute;
    top: 27px;
  }
  .panel--directions { left: 23px; width: 262px; }
  .panel--details { left: 932px; width: 236px; }
  .panel h2 {
    margin: 0;
    font-size: 15.5px;
    font-weight: 500;
    line-height: 20px;
  }
  .panel p {
    margin: 0;
    font-size: 15px;
    line-height: 20px;
  }
  .panel strong { font-weight: 500; }
  .cautions { margin-top: 16px; }
  .cautions h2 { font-size: 13.5px; line-height: 17px; }
  .cautions p { font-size: 13px; line-height: 17px; }
  .storage-heading { margin-top: 2px !important; }

  .claim-badges {
    position: absolute;
    left: 21px;
    top: 270px;
    display: flex;
    gap: 4px;
  }
  .claim-badge {
    width: 44px;
    height: 44px;
    border-radius: 50%;
    border: 2px solid var(--rose);
    box-sizing: border-box;
    display: flex;
    align-items: center;
    justify-content: center;
    text-align: center;
    font-size: 7px;
    line-height: 8px;
    font-weight: 700;
    letter-spacing: 0.2px;
    text-transform: uppercase;
    color: var(--rose);
    padding: 2px;
  }

  .brand-name {
    position: absolute;
    left: 0;
    width: 1166px;
    top: 30px;
    margin: 0;
    text-align: center;
    font-size: 52px;
    font-weight: 700;
    color: var(--rose-soft);
    line-height: 1;
  }
  .eco-seal {
    position: absolute;
    left: 765px;
    top: 69px;
    width: 56px;
    height: 56px;
    border-radius: 50%;
    border: 2px solid var(--rose);
    box-sizing: border-box;
  }
  .art-cane {
    position: absolute;
    left: 352px;
    top: 100px;
    width: 80px;
    height: 174px;
    background: linear-gradient(180deg, var(--illustration), #e5aec1);
    border-radius: 40px 40px 4px 4px;
    opacity: 0.75;
  }
  .art-leaves {
    position: absolute;
    left: 748px;
    top: 189px;
    width: 70px;
    height: 66px;
    background: #f3c6d6;
    border-radius: 50%;
  }
  .product-name {
    position: absolute;
    left: 400px;
    width: 420px;
    top: 144px;
    margin: 0;
    text-align: center;
    font-family: "Playfair Display", Georgia, serif;
    font-weight: 500;
    font-size: 44px;
    line-height: 1;
    color: var(--rose);
  }
  .product-type {
    position: absolute;
    left: 400px;
    width: 400px;
    top: 219px;
    text-align: center;
    font-size: 21px;
    font-weight: 400;
    line-height: 24px;
    color: var(--rose);
  }
  .skin-band {
    position: absolute;
    left: 394px;
    top: 274px;
    width: 412px;
    height: 26px;
    background: var(--rose);
    color: var(--band-text);
    font-size: 15px;
    font-weight: 400;
    line-height: 26px;
    text-align: center;
    box-sizing: border-box;
    padding-right: 24px;
  }
  .net-weight {
    position: absolute;
    left: 500px;
    width: 200px;
    top: 308px;
    text-align: center;
    font-size: 20px;
    line-height: 24px;
    font-weight: 400;
    color: var(--rose);
  }

  .care-icons {
    position: absolute;
    left: 934px;
    top: 298px;
    display: flex;
    align-items: center;
    gap: 10px;
  }
  .care-icons svg { display: block; }
</style>
</head>
<body>
<main class="label">

  <section class="panel panel--directions">
    <h2>Directions to use Body Sugar Scrub:</h2>
    <p>Apply to wet skin gently in a circular motion on desired body area, hands, feet, legs, arms, etc. Once you have a good scrub, rinse, pat dry, and enjoy soft, hydrated skin. Best to use in the shower. Use between 2-3 times a week if needed.</p>
    <div class="cautions">
      <h2>*Cautions:</h2>
      <p>(1) Allergy: Approach this product with extreme caution, if you have allergies</p>
      <p>(2) Avoid direct contact with eyes</p>
    </div>
  </section>

  <div class="claim-badges">
    <div class="claim-badge">All Natural</div>
    <div class="claim-badge">Cruelty Free</div>
    <div class="claim-badge">Vegan Free</div>
    <div class="claim-badge">No Mineral Oil</div>
    <div class="claim-badge">No Petro&shy;leum</div>
    <div class="claim-badge">No Para&shy;bens</div>
  </div>

  <div class="brand-name">Velvet Petal</div>
  <div class="eco-seal" aria-label="Eco friendly seal"></div>
  <div class="art-cane" role="img" aria-label="Sugarcane stalks illustration"></div>
  <div class="art-leaves" role="img" aria-label="Strawberry leaves illustration"></div>

  <h1 class="product-name">Calm Dune Hush</h1>
  <div class="product-type">Whipped<br>Body Sugar Scrub</div>
  <div class="skin-band">Ideal for all Skin Types</div>
  <div class="net-weight">8oz</div>

  <section class="panel panel--details">
    <h2>Ingredients:</h2>
    <p>Pure Cane Sugar, Extra Virgin Coconut Oil, Mango Butter, Kukum Butter, Emulsifying Wax, Jojoba Seed Oil, Sweet Almond Oil, Strawberry Essential Oil, and Pomegranate Essential Oil.</p>
    <h2 class="storage-heading">Storage/Shelf Life of Product:</h2>
    <p>For best results, stir/mix scrub with the wooden or plastic spoon before each use. The shelf life of all sugar scrubs is <strong>6-8 weeks</strong>.</p>
    <p>Keep the product in a cool, dry place, away from hot or heated temperatures.</p>
  </section>

  <div class="care-icons">
    <svg class="icon-open-jar" width="34" height="36" viewBox="0 0 34 36" aria-label="Use within 6-8 weeks after opening">
      <path d="M3 12 L27 2" stroke="#141414" stroke-width="2" fill="none"/>
      <path d="M4 16 h26 v14 a13 4 0 0 1 -26 0 z" fill="none" stroke="#141414" stroke-width="2"/>
      <ellipse cx="17" cy="16" rx="13" ry="3" fill="none" stroke="#141414" stroke-width="2"/>
      <text x="17" y="31" text-anchor="middle" font-family="Roboto Condensed, sans-serif" font-size="8" font-weight="700" fill="#141414">6-8 W</text>
    </svg>
    <svg class="icon-dispose" width="33" height="33" viewBox="0 0 33 33" aria-label="Dispose in bin">
      <rect x="1" y="1" width="31" height="31" fill="none" stroke="#141414" stroke-width="2"/>
      <path d="M7 15 h9 l-1.5 13 h-6 z" fill="#141414"/>
      <rect x="6" y="12" width="11" height="2" fill="#141414"/>
    </svg>
    <svg class="icon-recycle" width="32" height="32" viewBox="0 0 32 32" aria-label="Recyclable packaging">
      <circle cx="16" cy="16" r="14" fill="none" stroke="#141414" stroke-width="3"/>
      <path d="M10 20 a7 7 0 0 1 9 -10" fill="none" stroke="#141414" stroke-width="3"/>
      <path d="M17 6 l5 4 -5 4 z" fill="#141414"/>
    </svg>
  </div>

</main>
</body>
</html>
```